Business Card Design

I design and sell kitchens. I would like the card to have a black background either gloss or matt and a stripe through the middle in deep sky blue, the same blue as the team ridgeway pro cycling team. Written in the blue stripe in white i would like Harbourline kitchens in italics. underneath the stripe, again in white i would like 'the complete design and installation service. On the reverse i would like the following in simple black on white
Owen Tramley
07814 296540
email- owentramley@harbourlinekitchens-example.co.uk
Web- WWW.harbourlinekitchens-example.co.uk

I have added a copy of an initial idea for a logo but it can be changed to suit the brief above

Industry/Entity Type

Business

Contact Information for Business Card

Harbourline Kitchens
The complete design and installation service
Owen Tramley
07814 296540-mob
owentramley@harbourlinekitchen-example.co.uk
WWW.harbourlinekitchens-example.co.uk

```html
<!DOCTYPE html>
<html lang="en">
<head>
<meta charset="utf-8">
<title>Harbourline Kitchens – Business Card</title>
<link rel="stylesheet" href="https://fonts.googleapis.com/css2?family=Open+Sans:wght@400;700&family=Questrial&display=swap">
<style>
  :root {
    --backdrop: #e6e4e2;
    --card-black: #0b0b0b;
    --card-black-soft: #161616;
    --stripe-blue: #37a8e0;
    --text-white: #ffffff;
    --text-grey: #c9c9c9;
    --rule-grey: #8a8a8a;
  }
  * { box-sizing: border-box; margin: 0; padding: 0; }
  html, body {
    width: 1200px;
    height: 716px;
    overflow: hidden;
    background: var(--backdrop);
  }
  .canvas {
    position: relative;
    width: 1200px;
    height: 716px;
  }
  .card {
    position: absolute;
    top: 198px;
    width: 540px;
    height: 320px;
    background: var(--card-black);
    box-shadow: 0 10px 28px rgba(0,0,0,0.25);
    overflow: hidden;
  }
  .card--back { left: 40px; }
  .card--front {
    left: 620px;
    background: radial-gradient(ellipse at 50% 40%, var(--card-black-soft), var(--card-black) 75%);
  }

  /* Back: contact side */
  .contact-block {
    position: absolute;
    left: 0;
    right: 0;
    top: 128px;
    display: flex;
    justify-content: center;
    align-items: center;
    font-family: "Questrial", sans-serif;
    color: var(--text-grey);
  }
  .contact-name {
    font-size: 17px;
    letter-spacing: 0.5px;
    padding-right: 18px;
    align-self: flex-start;
    margin-top: 4px;
  }
  .contact-rule {
    width: 1px;
    height: 72px;
    background: var(--rule-grey);
  }
  .contact-list {
    list-style: none;
    padding-left: 14px;
    font-size: 10.5px;
    line-height: 20px;
  }
  .contact-list li {
    display: flex;
    align-items: center;
    gap: 8px;
  }
  .contact-icon {
    width: 11px;
    height: 11px;
    flex: none;
  }

  /* Front: brand side */
  .brand-stripe {
    position: absolute;
    left: 0;
    right: 0;
    top: 66px;
    height: 122px;
    background: var(--stripe-blue);
    display: flex;
    align-items: center;
    justify-content: center;
  }
  .brand-name {
    font-family: "Open Sans", sans-serif;
    font-weight: 700;
    font-size: 40px;
    color: var(--text-white);
    letter-spacing: 0.5px;
  }
  .brand-tagline {
    position: absolute;
    left: 0;
    right: 0;
    top: 198px;
    text-align: center;
    font-family: "Open Sans", sans-serif;
    font-size: 19px;
    color: var(--text-white);
  }
</style>
</head>
<body>
<main class="canvas">

  <section class="card card--back" aria-label="Business card, contact side">
    <div class="contact-block">
      <p class="contact-name">Owen Tramley</p>
      <div class="contact-rule"></div>
      <ul class="contact-list">
        <li>
          <svg class="contact-icon" viewBox="0 0 12 12" aria-hidden="true">
            <path d="M3 1 L5 3.5 L4 4.8 Q5 7 7.2 8 L8.5 7 L11 9 L9.6 11 Q4.5 10.5 1 3 Z" fill="#c9c9c9"/>
          </svg>
          <span>07814 296540</span>
        </li>
        <li>
          <svg class="contact-icon" viewBox="0 0 12 12" aria-hidden="true">
            <rect x="0.5" y="2.5" width="11" height="7" fill="#c9c9c9"/>
            <path d="M0.5 2.5 L6 6.5 L11.5 2.5" fill="none" stroke="#0b0b0b" stroke-width="1"/>
          </svg>
          <span>email- owentramley@harbourlinekitchens-example.co.uk</span>
        </li>
        <li>
          <svg class="contact-icon" viewBox="0 0 12 12" aria-hidden="true">
            <circle cx="6" cy="6" r="5" fill="none" stroke="#c9c9c9" stroke-width="1.2"/>
            <ellipse cx="6" cy="6" rx="2.2" ry="5" fill="none" stroke="#c9c9c9" stroke-width="1"/>
            <line x1="1" y1="6" x2="11" y2="6" stroke="#c9c9c9" stroke-width="1"/>
          </svg>
          <span>www.harbourlinekitchens-example.co.uk</span>
        </li>
      </ul>
    </div>
  </section>

  <section class="card card--front" aria-label="Business card, brand side">
    <div class="brand-stripe">
      <h1 class="brand-name">Harbourline Kitchens</h1>
    </div>
    <p class="brand-tagline">The complete design and installation service</p>
  </section>

</main>
</body>
</html>
```